radiant veil

Simple yet classy elegance look
website : www.radiantveil.example
https://www.facebook.com/radiantt.veil

Attachments are "preferences" I would like to have in similarity

Radiant Veil presents you the simplest ,classy yet modest suitable for the young and old alike with carefully selected clothing designs and strive to deliver the best customer experience .
To be the leading brand retail fashion at its best and optimizing shopping experience

Target Market(s)

Working ladies , middle to high income earners

Industry/Entity Type

Clothing

Font styles to use
Sans Serif
Decorative
Script

Requirements
Must have
• Simple but eye-catchy
Embossed and alphabetically words engulfed or surround with design

```html
<!DOCTYPE html>
<html lang="en">
<head>
<meta charset="UTF-8">
<title>Radiant Veil — Banner</title>
<link href="https://fonts.googleapis.com/css2?family=Tinos:wght@400&display=swap" rel="stylesheet">
<style>
  :root {
    --page-bg: #ffffff;
    --fabric-base: #ebebeb;
    --fabric-light: #f4f4f4;
    --fabric-shade: #dedede;
    --fabric-fold: rgba(255, 255, 255, 0.75);
    --ink-dark: #1f1f1f;
    --ink-mid: #4a4a4a;
    --ink-light: #7a7a7a;
    --emboss-highlight: rgba(255, 255, 255, 0.85);
  }
  * { margin: 0; padding: 0; box-sizing: border-box; }
  html, body {
    width: 1200px;
    height: 1000px;
    overflow: hidden;
    background: var(--page-bg);
  }
  .canvas {
    position: relative;
    width: 1200px;
    height: 1000px;
  }
  .banner {
    position: absolute;
    left: 208px;
    top: 422px;
    width: 785px;
    height: 157px;
    overflow: hidden;
  }
  .banner__fabric {
    position: absolute;
    inset: 0;
    background:
      linear-gradient(122deg, transparent 18%, var(--fabric-fold) 26%, transparent 31%),
      linear-gradient(118deg, transparent 28%, rgba(255,255,255,0.35) 33%, transparent 38%),
      linear-gradient(58deg, transparent 72%, rgba(255,255,255,0.55) 79%, transparent 84%),
      radial-gradient(ellipse at 50% 45%, var(--fabric-light) 0%, var(--fabric-base) 55%, var(--fabric-shade) 100%);
  }
  .banner__text {
    position: absolute;
    inset: 0;
    text-align: center;
    font-family: "Tinos", "Times New Roman", serif;
    font-weight: 400;
  }
  .brand-name,
  .tagline {
    position: absolute;
    left: 0;
    right: 0;
    display: block;
    font-weight: 400;
    line-height: 1;
    background: linear-gradient(180deg, var(--ink-light) 0%, var(--ink-dark) 50%, var(--ink-mid) 100%);
    -webkit-background-clip: text;
    background-clip: text;
    color: transparent;
    filter: drop-shadow(0 1px 0 var(--emboss-highlight));
  }
  .brand-name {
    top: 44px;
    font-size: 45px;
    letter-spacing: 0.5px;
  }
  .tagline {
    top: 102px;
    font-size: 24px;
  }
</style>
</head>
<body>
  <main class="canvas">
    <section class="banner">
      <div class="banner__fabric" role="img" aria-label="Draped white silk with a faint pale grey damask pattern"></div>
      <div class="banner__text">
        <h1 class="brand-name">Radiant Veil</h1>
        <p class="tagline">Fashion Simplicity</p>
      </div>
    </section>
  </main>
</body>
</html>
```